Test and Tag business card design

We are an appliance test and tag company in Brisbane Australia requiring a business card design.
I don't have a logo.
Card front: Matte black background with white font.
Card back: White background with black font colour
Examples are attached
Minimalist design
Reason: Looking for more designs with an extreme minimal feel
Industry/Entity Type
Appliance
Contact Information for Business Card
Business name: Harbor Check and Label
Description: Onsite Electrical Testing and Tagging
Licence No. 41853
Name: Greg Pellow
Mobile: 0418 526 937
Email: greg@harborcheckandlabel.com.au
Web: harborcheckandlabel.com.au
Logo Text
Harbor Check and Label
Look and feel

```html
<!DOCTYPE html>
<html lang="en">
<head>
<meta charset="utf-8">
<title>Harbor Check and Label — Business Card</title>
<link rel="stylesheet" href="https://fonts.googleapis.com/css2?family=Open+Sans:wght@400&family=Tinos&display=swap">
<style>
  :root {
    --backdrop: #d6d6d6;
    --card-white: #ffffff;
    --card-black: #050505;
    --ink-dark: #111111;
    --ink-light: #f4f4f4;
    --rule: #e8e8e8;
  }
  html, body {
    margin: 0;
    width: 1200px;
    height: 985px;
    overflow: hidden;
    background: var(--backdrop);
  }
  .canvas {
    position: relative;
    width: 1200px;
    height: 985px;
  }
  .card {
    position: absolute;
    left: 250px;
    width: 700px;
    height: 428px;
    border-radius: 26px;
    box-shadow: 0 10px 28px rgba(0,0,0,0.22);
    box-sizing: border-box;
  }
  .card--back {
    top: 44px;
    background: var(--card-white);
    color: var(--ink-dark);
  }
  .card--front {
    top: 513px;
    background: var(--card-black);
    color: var(--ink-light);
  }
  .brand {
    display: flex;
    align-items: center;
    gap: 10px;
    font-family: "Open Sans", sans-serif;
    font-weight: 400;
    line-height: 1;
  }
  .brand__square {
    width: 34px;
    height: 34px;
    background: currentColor;
    flex: none;
  }
  .card--back .brand {
    position: absolute;
    left: 150px;
    top: 150px;
    font-size: 44px;
  }
  .card--back .web {
    position: absolute;
    left: 150px;
    top: 250px;
    font-family: "Tinos", serif;
    font-size: 26px;
  }
  .front-logo {
    position: absolute;
    left: 56px;
    top: 40px;
    font-family: "Open Sans", sans-serif;
    font-weight: 400;
    font-size: 48px;
    line-height: 1.05;
  }
  .front-logo .brand { gap: 12px; }
  .front-logo .brand__square { width: 38px; height: 38px; }
  .front-logo__line2 { margin-left: 0; }
  .rule {
    position: absolute;
    left: 56px;
    top: 164px;
    width: 330px;
    height: 2px;
    background: var(--rule);
  }
  .tagline {
    position: absolute;
    left: 56px;
    top: 178px;
    font-family: "Open Sans", sans-serif;
    font-size: 22px;
  }
  .person {
    position: absolute;
    left: 56px;
    top: 240px;
    font-family: "Tinos", serif;
  }
  .person__name { font-size: 30px; margin: 0; font-weight: 400; }
  .person__licence { font-size: 16px; margin: 6px 0 0; }
  .contact {
    position: absolute;
    left: 300px;
    top: 300px;
    margin: 0;
    font-family: "Tinos", serif;
    font-size: 21px;
    line-height: 1.3;
    list-style: none;
    padding: 0;
  }
</style>
</head>
<body>
<main class="canvas">
  <section class="card card--back" aria-label="Card back">
    <div class="brand"><span class="brand__square"></span><span>Harbor Check &amp; Label</span></div>
    <p class="web" style="margin:0">harborcheckandlabel.com.au</p>
  </section>

  <section class="card card--front" aria-label="Card front">
    <div class="front-logo">
      <div class="brand"><span class="brand__square"></span><span>Harbor</span></div>
      <div class="front-logo__line2">Check &amp; Label</div>
    </div>
    <div class="rule"></div>
    <p class="tagline" style="margin:0">Onsite Electrical Testing and Tagging</p>
    <div class="person">
      <h2 class="person__name">Greg Pellow</h2>
      <p class="person__licence">Licence No. 41853</p>
    </div>
    <ul class="contact">
      <li>Mobile: 0418 526 937</li>
      <li>Email: greg@harborcheckandlabel.com.au</li>
      <li>Web: harborcheckandlabel.com.au</li>
    </ul>
  </section>
</main>
</body>
</html>
```